Verpackungen für Sekt/Champagner Flaschen
Zielgruppe
Dekoration für Hochzeiten. Tisch Dekoration für Hochzeiten. Zielgruppe alles was mit Hochzeiten zutun hat
Aufgabenstellung
Wir lassen gerade ein Tube/Dose herstellen, die als Umverpackung oder einfach Verpackung für Sekt/Champagne Flaschen dienen soll die dann auf die Tische für Hochzeit´s Deko kommt um die die Tisch Deko aufzubessern, statt einfach nur eine Sekt Flasche stehen zu haben. .Die Tube wird komplett in weiß sein und alles andere an Design soll in einem Gold sein. Mr&Mrs oder Just Married mit Herzen und alles was sonst dazu gehört, da lassen wir freie Hand.
Das Design soll Schlicht sein aber auch Luxuriös.
Durchmesser der Tube wird 8,5 cm haben und 34-35 cm sein.
Die Goldene Schrift und das Muster soll am Ende in einem Relief Lack auf der Tube erscheinen

```html
<!DOCTYPE html>
<html lang="de">
<head>
<meta charset="utf-8">
<title>Mr &amp; Mrs – Banderole Sektverpackung</title>
<link href="https://fonts.googleapis.com/css2?family=Cormorant+Garamond:wght@500&display=swap" rel="stylesheet">
<style>
  :root {
    --paper: #ffffff;
    --gold: #c49b74;
    --gold-text: #b08a64;
    --chocolate: #42200d;
  }
  html, body {
    margin: 0;
    padding: 0;
    width: 1200px;
    height: 283px;
    background: var(--paper);
    overflow: hidden;
  }
  .banderole {
    display: block;
    width: 1200px;
    height: 283px;
    background: var(--paper);
  }
  .stripe { fill: var(--gold); }
  .label-box { fill: var(--chocolate); stroke: var(--gold); stroke-width: 6; }
  .label-title {
    font-family: "Cormorant Garamond", serif;
    font-weight: 500;
    font-size: 76px;
    fill: var(--gold-text);
  }
</style>
</head>
<body>
<svg class="banderole" viewBox="0 0 1200 283" xmlns="http://www.w3.org/2000/svg">
  <g class="stripes-left">
    <rect class="stripe" x="0" y="125" width="437" height="7"/>
    <rect class="stripe" x="0" y="140" width="437" height="7"/>
    <rect class="stripe" x="0" y="156" width="437" height="7"/>
  </g>
  <g class="stripes-right">
    <rect class="stripe" x="763" y="125" width="437" height="7"/>
    <rect class="stripe" x="763" y="140" width="437" height="7"/>
    <rect class="stripe" x="763" y="156" width="437" height="7"/>
  </g>

  <g class="label">
    <rect class="label-box" x="437" y="42" width="326" height="200"/>
    <text class="label-title" x="600" y="168" text-anchor="middle" textLength="260" lengthAdjust="spacingAndGlyphs">Mr &amp; Mrs</text>
  </g>
</svg>
</body>
</html>
```